PLOVEN Business Card

Coastal Build Additions and Refits. I need a business card designed for this new high end renovation business. I would like the logo centered on the back side with the ABN (37 915 402 176) on the bottom right hand corner.

I would like the following information placed on the other side along with some customized pattern or design.

Derek Collwood
Director
Phone: 1300 480 957
Fax: (02) 8145 9021
Website: www.plovenbuilders.com.au
Email: d.collwood@plovenbuilders.com.au
PO Box 87,
Kelvinbrook NSW 2069

(FB Logo) PLOVEN - Coastal Build Additions and Refits

The final design should communicate professionalism and trust.

Back side background colour: white
Front side: Undecided

```html
<!DOCTYPE html>
<html lang="en">
<head>
<meta charset="UTF-8">
<title>PLOVEN Business Card</title>
<link href="https://fonts.googleapis.com/css2?family=Open+Sans:wght@300;400;600&display=swap" rel="stylesheet">
<style>
  :root {
    --backdrop: #dcd9d5;
    --card-white: #ffffff;
    --brand-blue: #1c6ea8;
    --label-blue: #2f7fc0;
    --pattern-blue: #cfe0ee;
    --ink: #3d3d3d;
    --muted: #7a7a7a;
    --soft-gray: #9a9a9a;
  }
  * { box-sizing: border-box; margin: 0; padding: 0; }
  html, body {
    width: 1200px;
    height: 800px;
    overflow: hidden;
    background: var(--backdrop);
    font-family: "Open Sans", Arial, sans-serif;
  }
  .stage {
    width: 1200px;
    height: 800px;
    display: flex;
    align-items: center;
    justify-content: center;
    gap: 60px;
  }
  .card {
    position: relative;
    width: 520px;
    height: 316px;
    overflow: hidden;
    background: var(--card-white);
    box-shadow: 0 6px 18px rgba(0,0,0,0.14);
  }
  .card-pattern {
    position: absolute;
    top: 0;
    right: 0;
    width: 220px;
    height: 316px;
  }
  .card-band {
    position: absolute;
    left: 0;
    bottom: 0;
    width: 100%;
    height: 10px;
    background: var(--brand-blue);
  }

  /* Contact side */
  .card--front { color: var(--ink); }
  .wordmark {
    position: absolute;
    top: 26px;
    left: 32px;
    font-size: 38px;
    font-weight: 600;
    letter-spacing: 2px;
    color: var(--brand-blue);
    line-height: 1;
  }
  .address {
    position: absolute;
    top: 88px;
    left: 32px;
    font-size: 12px;
    font-weight: 300;
    color: var(--muted);
    line-height: 1.45;
  }
  .contacts {
    position: absolute;
    top: 134px;
    left: 32px;
    list-style: none;
    font-size: 12px;
    font-weight: 300;
    line-height: 1.5;
    color: var(--ink);
  }
  .contacts .label { color: var(--label-blue); }
  .person {
    position: absolute;
    top: 134px;
    right: 32px;
    text-align: right;
    line-height: 1.15;
  }
  .person__name { font-size: 19px; font-weight: 400; color: var(--brand-blue); }
  .person__role { font-size: 16px; font-weight: 300; color: var(--muted); }
  .tagline-stack {
    position: absolute;
    right: 32px;
    bottom: 28px;
    text-align: right;
    font-size: 17px;
    font-weight: 400;
    line-height: 1.05;
    text-transform: uppercase;
    color: var(--soft-gray);
  }
  .tagline-stack .name { font-weight: 600; color: var(--muted); }
  .tagline-stack .accent { color: var(--label-blue); }

  /* Logo side */
  .card--back {
    display: flex;
    flex-direction: column;
    align-items: center;
    justify-content: center;
    gap: 10px;
  }
  .card--back .wordmark {
    position: static;
    font-size: 54px;
  }
  .back-web {
    font-size: 13px;
    font-weight: 300;
    letter-spacing: 2px;
    color: var(--muted);
  }
  .abn {
    position: absolute;
    right: 24px;
    bottom: 22px;
    font-size: 11px;
    font-weight: 400;
    letter-spacing: 1px;
    color: var(--muted);
  }
</style>
</head>
<body>
<main class="stage">
  <section class="card card--front" aria-label="Contact side">
    <svg class="card-pattern" viewBox="0 0 220 316" aria-hidden="true">
      <g stroke="var(--pattern-blue)" stroke-width="1.2" fill="none">
        <line x1="120" y1="0" x2="220" y2="100"/>
        <line x1="150" y1="0" x2="220" y2="70"/>
        <line x1="180" y1="0" x2="220" y2="40"/>
      </g>
    </svg>
    <div class="wordmark">PLOVEN</div>
    <p class="address">PO Box 87,<br>Kelvinbrook NSW 2069</p>
    <ul class="contacts">
      <li><span class="label">phone:</span> 1300 480 957</li>
      <li><span class="label">fax:</span> (02) 8145 9021</li>
      <li><span class="label">email:</span> d.collwood@plovenbuilders.com.au</li>
      <li><span class="label">website:</span> www.plovenbuilders.com.au</li>
    </ul>
    <div class="person">
      <p class="person__name">Derek Collwood</p>
      <p class="person__role">director</p>
    </div>
    <p class="tagline-stack">
      <span class="name">Ploven</span><br>
      Coastal <span class="accent">Build</span><br>
      <span class="accent">Additions</span><br>
      &amp; <span class="accent">Refits</span>
    </p>
    <div class="card-band"></div>
  </section>

  <section class="card card--back" aria-label="Logo side">
    <svg class="card-pattern" viewBox="0 0 220 316" aria-hidden="true">
      <g stroke="var(--pattern-blue)" stroke-width="1.2" fill="none">
        <line x1="120" y1="0" x2="220" y2="100"/>
        <line x1="150" y1="0" x2="220" y2="70"/>
        <line x1="180" y1="0" x2="220" y2="40"/>
      </g>
    </svg>
    <div class="wordmark">PLOVEN</div>
    <p class="back-web">www.plovenbuilders.com.au</p>
    <p class="abn">ABN 37 915 402 176</p>
    <div class="card-band"></div>
  </section>
</main>
</body>
</html>
```